We have 'joined together' 6 micro-sites with a common theme. Looking to upgrade the design of a total of 26 pages on the abovementioned sites, whilst maintaining a common look and feel.

Goal is to improve customer experience and conversion rate, whilst maintaining Vantro rankings. New design to be responsive to different devices and SEO optimised

We prefer simple designs with the cleaness of Zelqo.com, however with more descriptive text. Target audience are business managers and owners, so site should convey professional capability, with a hint of playfulness. After all data can be fun? No?

See attached doc for further details.

Update: 19/8/2014. Following further consideration, the HTML coding no longer required. Once design is finalised, we require a PSD file for each page showing the full page layout, including all images and icons. We will extract the relevant bits from the PSD and do the coding and css inhouse.
Updates

Hi All The Pelquin Collective - PSD Design Only. HTML no longer required Following further consideration, the HTML / Css coding aspect of the project NO longer required. Once design is finalised, we require a PSD file from you for each of the 26 web pages, showing the page layout and including all images and icons. If one page layout is the same as another, then we request that you just supply images and icons for that page in a PSD file. We will then extract the relevant bits from the PSD and we will do the coding and css inhouse. Our main aim is to get an awesome, blow-your-sox-off design that compels users to convert. Many thanks in anticipation Oliver.

Project Deadline Extended
Reason: Changed deliverables from PSD, HTML and Coding t o PSD only. Hopefully this change will allow previous designers who were not interested to reconsider. Many thanks Oliver

Target Market(s)

Target market is business & IT managers within Australian organisations who are having problems with their data. Site must convey the impression that we are:
1) Very capable
2) Professional in our dealings
3) Reliable & trustworthy
4) Just a little bit quirky

Aprox. 60% of users are female, 40% male. Typically in the 30 to 55 year old bracket.

Number 1 requirements is that we don't embarrass our clients in any way.
2nd is that we do a good high quality job, delivering a good result.

We are not the cheapest nor the most expensive data shop around. We offer good value-for-money solutions. We are also reliable, friendly and available

Industry/Entity Type

Business

Font styles to use
Sans Serif

Requirements
Must have
• Simple yet information dense design. The "who we are" and "what we do" to be immediately visible above the fold. Images to be high quality. Good usability.
Simple navigation structure. Easy for users to find the info that they want.

In summary a simple, but good looking site, that compels users to contact us
Should not have
• No flash, fancy automation, rotating images, pop-ups etc.

```html
<!DOCTYPE html>
<html lang="en">
<head>
<meta charset="utf-8">
<title>The Pelquin Collective – extract value from your data</title>
<link rel="stylesheet" href="https://fonts.googleapis.com/css2?family=Montserrat:wght@700&family=Open+Sans:wght@400;600&family=Source+Sans+3:wght@400;600;700&display=swap">
<style>
:root{
  --ink:#173a40;
  --orange:#e95f0c;
  --teal:#8ec6bb;
  --teal-pale:#deeeeb;
  --grey-pale:#f3f3f3;
  --text:#4a4a4a;
  --white:#ffffff;
}
*{margin:0;padding:0;box-sizing:border-box}
html,body{width:1200px;height:900px;overflow:hidden;background:#fff}
body{font-family:"Source Sans 3",Arial,sans-serif;color:var(--text)}
.page{position:absolute;left:336px;top:0;width:528px;height:900px;background:#fff;box-shadow:0 0 6px rgba(0,0,0,.18)}
.abs{position:absolute}

/* header */
.site-header{left:0;top:0;width:528px;height:34px;background:var(--ink)}
.brand{left:54px;top:10px;font-size:10px;font-weight:600;letter-spacing:.3px;color:var(--white);display:flex;align-items:center;gap:5px}
.brand-dot{width:7px;height:7px;border-radius:50%;background:var(--orange)}
.main-nav{left:255px;top:13px;display:flex;gap:17px;font-family:"Open Sans",Arial,sans-serif;font-size:6.5px;font-weight:600;color:var(--white)}
.main-nav .current{color:var(--orange)}
.call-box{left:387px;top:0;width:84px;height:41px;background:var(--orange);color:var(--white);text-align:center;padding-top:7px;line-height:13px}
.call-box .label{font-size:11px;display:block}
.call-box .number{font-size:11px;font-weight:700;display:block}

/* hero */
.hero{left:0;top:34px;width:528px;height:317px;background:
  radial-gradient(ellipse at 50% 55%,#b49a5e 0%,#7c6a3e 35%,#4b3f26 75%,#2f271a 100%)}
.hero-title{left:0;top:91px;width:528px;text-align:center;font-family:Montserrat,Arial,sans-serif;font-weight:700;font-size:18px;color:var(--white)}
.hero-lead{left:0;top:130px;width:528px;text-align:center;font-family:"Open Sans",Arial,sans-serif;font-size:14px;line-height:20px;color:var(--white)}
.service{top:265px;width:71px;height:71px;border-radius:50%;background:var(--teal);text-align:center;color:var(--ink)}
.service.active{background:var(--orange);color:var(--white)}
.service svg{display:block;margin:11px auto 0;width:26px;height:26px}
.service span{display:block;font-size:8.5px;margin-top:4px}

/* testimonials */
.band{left:0;width:528px;text-align:center;font-weight:700;font-size:13px;color:var(--ink)}
.testimonials-head{top:351px;height:45px;background:var(--teal);line-height:45px}
.testimonials{left:0;top:396px;width:528px;height:152px;background:var(--grey-pale)}
.quote-mark{font-family:Georgia,serif;font-size:50px;font-weight:700;color:var(--teal);line-height:1}
.quote-text{width:172px;font-size:8px;line-height:12px;color:#666}
.quote-by{font-size:8px;color:var(--ink);font-weight:600}

/* blog */
.blog{left:0;top:548px;width:528px;height:183px;background:var(--teal-pale)}
.blog-head{top:20px;background:none}
.post{top:62px;width:132px}
.post h3{font-size:9px;font-weight:400;color:var(--orange);margin-bottom:8px}
.post p{font-family:"Open Sans",Arial,sans-serif;font-size:6.3px;line-height:12.3px;color:#333;height:57px}
.post a{font-size:6.5px;color:var(--orange);text-decoration:none}

/* contact */
.contact{left:0;top:731px;width:528px;height:135px;background:var(--orange);color:var(--white)}
.contact h4{position:absolute;left:70px;top:27px;font-size:6.8px;font-weight:700}
.contact-list{position:absolute;left:56px;top:47px;list-style:none;font-family:"Open Sans",Arial,sans-serif;font-size:6.2px;line-height:10.5px}
.contact-list li{display:flex;gap:6px}
.contact-list svg{width:6px;height:6px;margin-top:2px;flex:none}
.form-label{font-size:6.5px}
.field{background:var(--white)}
.send{left:339px;top:96px;width:41px;height:12px;background:var(--teal);color:var(--ink);font-size:6px;font-weight:700;display:flex;align-items:center;justify-content:center;gap:6px}

/* footer */
.site-footer{left:0;top:866px;width:528px;height:34px;background:var(--ink);color:var(--white);font-size:5px}
.social{width:6px;height:6px;border-radius:50%;background:var(--white);top:14px}
</style>
</head>
<body>
<div class="page">

  <header class="abs site-header">
    <div class="abs brand"><span>THE PELQUIN COLLECTIVE</span><span class="brand-dot"></span></div>
    <nav class="abs main-nav"><span class="current">HOME</span><span>BLOG</span><span>CONTACT US</span></nav>
  </header>
  <div class="abs call-box"><span class="label">Call Us</span><span class="number">1300-555-014</span></div>

  <section class="abs hero" role="img" aria-label="Warm-toned photograph of a long library hall lined with bookshelves"></section>
  <h1 class="abs hero-title">extract value from your data.</h1>
  <p class="abs hero-lead">we are solving business problems that require<br>complex data analysis, cleansing, mining or modelling<br>techniques.</p>

  <div class="abs service active" style="left:56px">
    <svg viewBox="0 0 26 26" fill="#fff"><rect x="3" y="16" width="4" height="8"/><rect x="9" y="13" width="4" height="11"/><rect x="15" y="10" width="4" height="14"/><rect x="21" y="7" width="4" height="17"/><polyline points="3,11 9,7 14,9 22,3" fill="none" stroke="#fff" stroke-width="1.6"/><circle cx="22" cy="3" r="1.6"/></svg>
    <span>Data Analysis</span>
  </div>
  <div class="abs service" style="left:142px">
    <svg viewBox="0 0 26 26" fill="none" stroke="#173a40" stroke-width="1.8"><line x1="23" y1="2" x2="14" y2="13"/><path d="M10 12l6 5-4 7c-3 0-7-3-9-6z" fill="#173a40"/><circle cx="6" cy="5" r="1" fill="#173a40"/><circle cx="10" cy="3" r="1" fill="#173a40"/></svg>
    <span>Data Cleansing</span>
  </div>
  <div class="abs service" style="left:228px">
    <svg viewBox="0 0 26 26" fill="none" stroke="#173a40" stroke-width="2"><circle cx="11" cy="10" r="8"/><line x1="17" y1="16" x2="24" y2="24" stroke-width="3.5"/><line x1="7" y1="10" x2="15" y2="10"/><line x1="11" y1="6" x2="11" y2="14"/></svg>
    <span>Data Mining</span>
  </div>
  <div class="abs service" style="left:314px">
    <svg viewBox="0 0 26 26" fill="none" stroke="#173a40" stroke-width="2"><rect x="2" y="3" width="22" height="15" rx="1"/><line x1="13" y1="18" x2="13" y2="22"/><line x1="7" y1="23" x2="19" y2="23"/><circle cx="13" cy="10" r="2.5" fill="#173a40"/></svg>
    <span>Data Scraping</span>
  </div>
  <div class="abs service" style="left:400px">
    <svg viewBox="0 0 26 26" fill="#173a40"><ellipse cx="13" cy="5" rx="10" ry="3.5"/><path d="M3 8c0 2 4.5 3.5 10 3.5S23 10 23 8v4c0 2-4.5 3.5-10 3.5S3 14 3 12z"/><path d="M3 16c0 2 4.5 3.5 10 3.5S23 18 23 16v4c0 2-4.5 3.5-10 3.5S3 22 3 20z"/></svg>
    <span>Data Warehouse</span>
  </div>

  <h2 class="abs band testimonials-head">CLIENT TESTIMONIALS</h2>
  <section class="abs testimonials">
    <div class="abs quote-mark" style="left:56px;top:36px">&ldquo;</div>
    <p class="abs quote-text" style="left:93px;top:36px">I recommend Oliver for his attention to detail, his willingness to please the customer and get the job done. I'm sure he would be valued for any other business who is looking to find better solutions for analysing company performance etc.</p>
    <p class="abs quote-by" style="left:93px;top:108px">MARGO T – Accountant</p>
    <div class="abs quote-mark" style="left:268px;top:36px">&ldquo;</div>
    <p class="abs quote-text" style="left:305px;top:36px">We were blown away by your professionalism, rapid turnaround time and high level of matching accuracy. I can't thank you enough and have no regrets in recommending you to anybody who asks.</p>
    <p class="abs quote-by" style="left:305px;top:108px">DENIS K – Product Data Consultant</p>
  </section>

  <section class="abs blog">
    <h2 class="abs band blog-head">RECENT BLOG</h2>
    <article class="abs post" style="left:57px">
      <h3>Liability, Movement &amp; Man Hours</h3>
      <p>This dashboard-style report offers rapid comparison of project labour hours/spend at the different overtime rates, labour hours/spend by Project, cumulated leave liability and attrition rates.</p>
      <a href="#">READ MORE ...</a>
    </article>
    <article class="abs post" style="left:199px">
      <h3>Spend and Head Count</h3>
      <p>Provides month and year-to-date labour spend and head count data (columns), allocated by Cost Centre (rows). Includes permanent and non-permanent employees. Actual, Budget and Variance data</p>
      <a href="#">READ MORE ...</a>
    </article>
    <article class="abs post" style="left:341px">
      <h3>Profit &amp; Loss Report by GL Code</h3>
      <p>Provides 12 months of P&amp;L data for the selected financial year (columns), allocated to the general ledger structure (rows). This report is used to display Actual, Budget or combined Actual and Budget data.</p>
      <a href="#">READ MORE ...</a>
    </article>
  </section>

  <section class="abs contact">
    <h4>CONTACT US</h4>
    <ul class="contact-list">
      <li><svg viewBox="0 0 6 6" fill="none" stroke="#fff" stroke-width=".8"><path d="M3 5.6L1 3a2 2 0 1 1 4 0z"/></svg><span>14 Larkmoor Lane, Ashbury Vale,<br>Victoria, 3199, Australia</span></li>
      <li><svg viewBox="0 0 6 6" fill="none" stroke="#fff" stroke-width=".8"><rect x="1.5" y=".5" width="3" height="5" rx=".5"/></svg><span>1300 555 014</span></li>
      <li><svg viewBox="0 0 6 6" fill="none" stroke="#fff" stroke-width=".8"><rect x=".5" y="1" width="5" height="4"/><polyline points=".5,1 3,3.3 5.5,1"/></svg><span>info@pelquin.com.au</span></li>
      <li><svg viewBox="0 0 6 6" fill="none" stroke="#fff" stroke-width=".8"><circle cx="3" cy="3" r="2.5"/><line x1=".5" y1="3" x2="5.5" y2="3"/></svg><span>www.pelquin.com.au</span></li>
    </ul>
    <span class="abs form-label" style="left:199px;top:28px">Your Name</span>
    <div class="abs field" style="left:198px;top:42px;width:132px;height:14px"></div>
    <span class="abs form-label" style="left:199px;top:60px">Your Name</span>
    <div class="abs field" style="left:198px;top:73px;width:132px;height:14px"></div>
    <span class="abs form-label" style="left:340px;top:27px">Describe Project</span>
    <div class="abs field" style="left:339px;top:42px;width:132px;height:45px"></div>
    <div class="abs send">SEND <svg width="4" height="5" viewBox="0 0 4 5"><polyline points="1,.5 3,2.5 1,4.5" fill="none" stroke="#173a40" stroke-width="1"/></svg></div>
  </section>

  <footer class="abs site-footer">
    <span class="abs" style="left:57px;top:14px">© 2014 The Pelquin Collective</span>
    <span class="abs" style="left:198px;top:14px">Comments Policy &nbsp;|&nbsp; Disclaimer &nbsp;|&nbsp; Privacy Statement</span>
    <span class="abs social" style="left:332px"></span>
    <span class="abs social" style="left:359px"></span>
    <span class="abs social" style="left:383px"></span>
    <span class="abs social" style="left:408px"></span>
    <span class="abs" style="left:430px;top:13px;display:flex;gap:4px;align-items:center"><svg width="5" height="4" viewBox="0 0 5 4"><polyline points=".5,3.5 2.5,1 4.5,3.5" fill="none" stroke="#fff" stroke-width="1"/></svg>BACK TO TOP</span>
  </footer>

</div>
</body>
</html>
```